依頼詳細
自社に関わってくださっている顧客の皆様と各企業様あてに感謝が伝えられるような年賀状を作っていただきたいと思っています。
記載項目
前年に同じ
希望イメージ
シンプル 複雑
単色 カラフル
暗い 明るい
日常 高級
遊び心 厳粛
未来的 伝統的
女性的 男性的
希望する色
赤系
納品ファイル
• 高解像度JPG (.jpg)
• イラストレーター形式 (.ai)
• フォトショップ形式 (.psd)
• PNG形式 (.png)
補足説明
たくさんの応募ありがとうございます。
どの作品も素敵なのですが過去に扱ったデザインと似たものが多く決定に至りません。
そこで我が社のロゴをメインにした年賀状にしてみたらと考えなおしたのですが可能でしょうか。
お手数をおかけしますが何卒よろしくお願い申し上げます。
今月末までの締め切り日に変更させていただきました。
■ 選んだ理由

シンプルかつ爽やかで明るい未来を感じさせてくれるこちらのデザインに決定させていただきました。ロゴも見やすく気に入りました。ありがとうございました。
記載内容に追加をしていただきたいことがありますのでご相談に乗っていただければ幸いです。引き続きどうぞよろしくお願いいたします。

■ 提案者全員のお礼・コメント

この度は本当にたくさんの素敵なデザインをご応募いただきましてありがとうございました。
社員一同心より申し上げます。
どのデザインも甲乙つけがたい魅力がそれぞれにあり皆様の技術とセンスに感激しました。
またの機会がありました時にはまたお力を貸していただければ幸いです。
皆様のますますのご活躍をお祈りしつつお礼とさせていただきます。
ありがとうございました。

```html
<!DOCTYPE html>
<html lang="ja">
<head>
<meta charset="UTF-8">
<title>年賀状 2023 株式会社 青葉運輸</title>
<link rel="stylesheet" href="https://fonts.googleapis.com/css2?family=Noto+Sans+JP:wght@400;500;700;900&family=Roboto:wght@900&display=swap">
<style>
  :root {
    --blue-deep: #0b3c94;
    --blue-main: #1656b8;
    --blue-bright: #2a86dc;
    --cyan: #3fb6e6;
    --yellow: #f2e23a;
    --navy-text: #1c2f6e;
    --white: #ffffff;
  }
  * { margin: 0; padding: 0; box-sizing: border-box; }
  html, body { width: 809px; height: 1200px; overflow: hidden; background: var(--white); }
  body { font-family: "Noto Sans JP", sans-serif; }
  .card { position: relative; width: 809px; height: 1200px; overflow: hidden; }
  .card-bg { position: absolute; inset: 0; width: 809px; height: 1200px; }

  .greeting-head { position: absolute; top: 48px; left: 70px; display: flex; align-items: center; gap: 30px; color: var(--white); }
  .greeting-head__english { font-family: "Roboto", sans-serif; font-weight: 900; font-size: 36px; line-height: 1.02; letter-spacing: 1px; }
  .greeting-head__year { font-family: "Roboto", sans-serif; font-weight: 900; font-size: 158px; line-height: 1; letter-spacing: -2px; }

  .message { position: absolute; top: 278px; left: 0; width: 809px; text-align: center; color: var(--navy-text); font-weight: 500; font-size: 21px; line-height: 1.75; }
  .message__date { margin-top: 4px; font-weight: 700; }

  .brand-mark { position: absolute; top: 470px; left: 0; width: 809px; display: flex; justify-content: center; align-items: center; gap: 22px; }
  .brand-mark__dot { width: 54px; height: 54px; border-radius: 50%; background: var(--blue-main); }
  .brand-mark__name { font-weight: 700; font-size: 54px; color: var(--blue-main); letter-spacing: 2px; }

  .thanks { position: absolute; top: 818px; left: 50px; color: var(--blue-main); font-weight: 900; font-size: 31px; line-height: 1.45; letter-spacing: 1px; }

  .truck-visual { position: absolute; top: 936px; left: 42px; width: 172px; height: 92px; background: linear-gradient(180deg, #2e4d8e, #1d3466); border-radius: 6px; }

  .company { position: absolute; top: 1070px; left: 50px; color: var(--white); font-weight: 900; font-size: 33px; letter-spacing: 3px; padding-bottom: 6px; border-bottom: 3px solid var(--white); white-space: nowrap; }

  .contact { position: absolute; top: 1044px; left: 418px; width: 380px; color: var(--white); font-size: 19px; line-height: 1.5; font-weight: 500; font-style: normal; white-space: nowrap; }
  .contact__row { display: flex; align-items: center; gap: 5px; white-space: nowrap; }
  .contact__pair { display: flex; gap: 18px; }
  .contact__icon { width: 17px; height: 17px; flex: none; }
</style>
</head>
<body>
<main class="card">
  <svg class="card-bg" viewBox="0 0 809 1200" aria-hidden="true">
    <defs>
      <linearGradient id="bgBlue" x1="0" y1="0" x2="1" y2="1">
        <stop offset="0" stop-color="var(--blue-deep)"/>
        <stop offset="0.5" stop-color="var(--blue-main)"/>
        <stop offset="1" stop-color="var(--blue-deep)"/>
      </linearGradient>
      <linearGradient id="sweepRight" x1="1" y1="0" x2="0" y2="1">
        <stop offset="0" stop-color="var(--yellow)"/>
        <stop offset="0.45" stop-color="var(--cyan)"/>
        <stop offset="1" stop-color="var(--blue-main)"/>
      </linearGradient>
      <linearGradient id="sweepLeft" x1="0" y1="0" x2="1" y2="0">
        <stop offset="0" stop-color="var(--yellow)"/>
        <stop offset="0.5" stop-color="var(--cyan)" stop-opacity="0.6"/>
        <stop offset="1" stop-color="var(--white)" stop-opacity="0"/>
      </linearGradient>
    </defs>
    <rect width="809" height="1200" fill="url(#bgBlue)"/>
    <path d="M560 0 C 650 40 740 40 809 20 L809 0 Z" fill="var(--white)" opacity="0.85"/>
    <path d="M809 500 C 700 560 560 640 500 760 C 460 860 460 980 420 1040 L809 1040 Z" fill="url(#sweepRight)"/>
    <path d="M0 238 C 250 300 560 200 809 262 L809 560 C 660 600 520 690 480 800 C 450 900 420 990 380 1040 L0 1040 Z" fill="var(--white)"/>
    <path d="M0 770 C 120 760 260 790 360 800 C 250 820 120 820 0 845 Z" fill="url(#sweepLeft)"/>
    <path d="M0 1040 L809 1040" stroke="var(--blue-bright)" stroke-width="3"/>
  </svg>

  <header class="greeting-head">
    <div class="greeting-head__english">HAPPY<br>NEW<br>YEAR</div>
    <div class="greeting-head__year">2023</div>
  </header>

  <section class="message">
    <p>旧年中は格別のお引き立てを賜り厚く御礼申し上げます。</p>
    <p>本年も変わらぬご愛顧のほど何卒宜しくお願い申し上げます。</p>
    <p class="message__date">令和５年　元旦</p>
  </section>

  <div class="brand-mark">
    <span class="brand-mark__dot"></span>
    <span class="brand-mark__name">Aoba Unyu</span>
  </div>

  <p class="thanks">ご縁をいただいた皆さまに<br>真心こめて・・・</p>

  <div class="truck-visual" role="img" aria-label="トラックのイラスト"></div>

  <p class="company">株式会社 青葉運輸</p>

  <address class="contact">
    <div class="contact__row">〒012-3456</div>
    <div class="contact__row">○○県○○市○○町1-2-3456</div>
    <div class="contact__pair">
      <span class="contact__row">
        <svg class="contact__icon" viewBox="0 0 24 24"><path fill="#fff" d="M6.6 10.8a15 15 0 0 0 6.6 6.6l2.2-2.2c.3-.3.7-.4 1-.2 1.1.4 2.3.6 3.6.6.6 0 1 .4 1 1V20c0 .6-.4 1-1 1A17 17 0 0 1 3 4c0-.6.4-1 1-1h3.5c.6 0 1 .4 1 1 0 1.3.2 2.5.6 3.6.1.3 0 .7-.2 1z"/></svg>
        01-2345-6789
      </span>
      <span class="contact__row">
        <svg class="contact__icon" viewBox="0 0 24 24"><path fill="#fff" d="M6 3h9v5H6zM4 9h16a1 1 0 0 1 1 1v8h-4v3H7v-3H3v-8a1 1 0 0 1 1-1zm5 7v3h6v-3z"/></svg>
        01-2345-6780
      </span>
    </div>
    <div class="contact__row">https://○○○○○○○.jp/</div>
  </address>
</main>
</body>
</html>
```